Business Cards for an 'affordable luxury' inner city home builder in Calgary.

We need a business card design that emulates the progressive, innovative, culture of our company and the modern style of our homes. Use our website www.velmarcrest-ab.com as a reference for the product we build.

Our company builds homes in the inner city space of Calgary, Alberta. We build affordable luxury.

Target Market(s)

Young professional Families

Contact Information for Business Card

Try to maintain consistency with the logo font and the card font.

Requirements
Must have
• The details must include: Name, education, title, phone number, website and email (Address is not as important)
• The design must be uniques (like our logo), elegant, sophisticated and modern.

```html
<!DOCTYPE html>
<html lang="en">
<head>
<meta charset="utf-8">
<title>Velmarcrest Homes – Business Card</title>
<link href="https://fonts.googleapis.com/css2?family=Lato:wght@400;700;900&display=swap" rel="stylesheet">
<style>
  :root {
    --backdrop: #d9d9d9;
    --card-light: #fbf7f7;
    --card-dark: #232323;
    --ink: #1b1b1b;
    --ink-soft: #444444;
    --rule: #9a9a9a;
    --band-dark: #1e1e1e;
    --band-grey: #8a8a8a;
    --on-dark: #f2f2f2;
  }
  * { margin: 0; padding: 0; box-sizing: border-box; }
  html, body { width: 1200px; height: 782px; overflow: hidden; }
  body {
    background: var(--backdrop);
    font-family: "Lato", sans-serif;
    color: var(--ink);
    position: relative;
  }
  .card {
    position: absolute;
    top: 240px;
    width: 520px;
    height: 298px;
    overflow: hidden;
    box-shadow: 0 6px 18px rgba(0,0,0,0.22);
  }
  .card--front { left: 60px; background: var(--card-light); }
  .card--back { left: 620px; background: var(--card-dark); }

  /* Front */
  .brand {
    position: absolute;
    left: 40px;
    top: 92px;
    display: flex;
    align-items: flex-start;
    gap: 10px;
  }
  .brand__mark {
    width: 12px; height: 12px;
    background: var(--ink);
    margin-top: 4px;
  }
  .brand__name {
    font-weight: 700;
    font-size: 19px;
    line-height: 1.05;
    letter-spacing: 0.5px;
    text-transform: uppercase;
    color: var(--ink);
  }
  .divider {
    position: absolute;
    left: 262px;
    top: 82px;
    width: 1px;
    height: 116px;
    background: var(--rule);
  }
  .person {
    position: absolute;
    left: 282px;
    top: 84px;
  }
  .person__name {
    font-weight: 700;
    font-size: 20px;
    letter-spacing: 0.6px;
    text-transform: uppercase;
    line-height: 1;
  }
  .person__title {
    font-size: 13px;
    color: var(--ink-soft);
    margin-top: 3px;
    letter-spacing: 0.3px;
  }
  .contacts {
    list-style: none;
    margin-top: 16px;
  }
  .contacts li {
    display: flex;
    align-items: center;
    gap: 8px;
    font-size: 14px;
    line-height: 1.5;
    letter-spacing: 0.3px;
  }
  .contacts svg { width: 11px; height: 11px; flex: none; fill: var(--ink); }
  .bands {
    position: absolute;
    left: 0; bottom: 0;
    width: 520px; height: 34px;
  }

  /* Back */
  .back-pattern {
    position: absolute;
    inset: 0;
    background: linear-gradient(135deg, #262626, #202020);
  }
  .back-brand {
    position: absolute;
    left: 0; right: 0;
    top: 210px;
    text-align: center;
    font-weight: 700;
    font-size: 15px;
    letter-spacing: 1.5px;
    text-transform: uppercase;
    color: var(--on-dark);
  }
</style>
</head>
<body>

  <section class="card card--front">
    <div class="brand">
      <span class="brand__mark"></span>
      <span class="brand__name">Velmarcrest<br>Homes Ltd</span>
    </div>

    <div class="divider"></div>

    <div class="person">
      <h1 class="person__name">Adrian Kessler</h1>
      <p class="person__title">Managing Director</p>
      <ul class="contacts">
        <li>
          <svg viewBox="0 0 12 12" aria-hidden="true"><path d="M2 1h2.5l1 2.5-1.5 1a6 6 0 0 0 3.5 3.5l1-1.5 2.5 1V10a1 1 0 0 1-1 1A9 9 0 0 1 1 2a1 1 0 0 1 1-1z"/></svg>
          044-987 654 321
        </li>
        <li>
          <svg viewBox="0 0 12 12" aria-hidden="true"><path d="M0 2h12v8H0z M0.8 2.6 6 6.6l5.2-4" stroke="#fbf7f7" stroke-width="0.9"/></svg>
          info@velmarcrest-ab.com
        </li>
        <li>
          <svg viewBox="0 0 12 12" aria-hidden="true"><circle cx="6" cy="6" r="5.5"/><path d="M0.5 6h11M6 0.5c-3 3-3 8 0 11M6 0.5c3 3 3 8 0 11" stroke="#fbf7f7" stroke-width="0.8" fill="none"/></svg>
          www.velmarcrest-ab.com
        </li>
      </ul>
    </div>

    <svg class="bands" viewBox="0 0 520 34" aria-hidden="true">
      <polygon points="0,22 228,22 218,34 0,34" fill="var(--band-dark)"/>
      <polygon points="244,4 520,4 520,34 228,34" fill="var(--band-grey)"/>
      <polygon points="236,10 244,4 244,10" fill="#ffffff"/>
    </svg>
  </section>

  <section class="card card--back">
    <div class="back-pattern" role="img" aria-label="Repeating tone-on-tone house outline pattern across a charcoal background"></div>
    <p class="back-brand">Velmarcrest Homes Ltd</p>
  </section>

</body>
</html>
```